Fun conversation piece for the home depicting the history of the ownership (title) and more!

We need some ideas for a framed display to be hung in a home for a new company I started called Ledger of Hearth, LLC. We will create framed (or unframed canvass) wall displays depicting the Ledger of the Hearth (title transfers) with some interesting background on the subdivision the home is located. This will be a conversation piece. Use color if you feel that works best. I am envisioning perhaps the writing to be in old English or old Spanish font to reflect the history of Florida where I am located. I am wanting to incorporate perhaps a picture of the home converted into sketch as a background to the "history". Or we could skip that and use the vegetation (trees) native to the area for a background. I am going to attach something I found online as a sample but I am open to ideas. The sample is a little formal for what I am trying to do. I may sell these framed or as unframed canvass pictures which might need to be a bit more contemporary. I also need a logo if you have any ideas. LH in some form of old English style perhaps? The document attached labeled "Marrowbrook" is an example of the content I will be creating for the picture.
Updates

I misspelled "States" in one of the paragraphs. Can you correct that for me? United States. Not "sates". My bad.

Logo Text

Ledger of Hearth (or LH). Surprise me.

```html
<!DOCTYPE html>
<html lang="en">
<head>
<meta charset="utf-8">
<title>Marrowbrook — Ledger of Hearth</title>
<link rel="stylesheet" href="https://fonts.googleapis.com/css2?family=Cinzel:wght@700&family=IM+Fell+English+SC&family=Old+Standard+TT:ital,wght@0,400;0,700;1,400&display=swap">
<style>
  :root {
    --backdrop: #f4ecd9;
    --frame-dark: #3a2414;
    --frame-mid: #6b4526;
    --frame-gold: #b58a4a;
    --paper-light: #f3e6c6;
    --paper-mid: #e7d3a6;
    --paper-edge: #c9a66c;
    --ink: #2b1d12;
    --ink-title: #3a2616;
    --cap-green: #3f5a2c;
    --cap-red: #8c2f1c;
    --house-light: #e2d2ae;
    --house-dark: #b7a27c;
  }
  * { box-sizing: border-box; margin: 0; padding: 0; }
  html, body { width: 855px; height: 1200px; overflow: hidden; }
  body { background: var(--backdrop); position: relative; font-family: "Old Standard TT", "Times New Roman", serif; color: var(--ink); }

  .frame {
    position: absolute; left: 30px; top: 22px; width: 795px; height: 1160px;
    border-radius: 18px;
    background: var(--frame-dark);
    box-shadow: 0 0 0 3px var(--frame-mid) inset;
  }
  .parchment {
    position: absolute; left: 70px; top: 62px; width: 715px; height: 1080px;
    border-radius: 6px;
    background: radial-gradient(ellipse at 50% 45%, var(--paper-light) 0%, var(--paper-mid) 70%, var(--paper-edge) 100%);
    box-shadow: 0 0 0 2px var(--frame-gold);
  }

  .content {
    position: absolute; left: 142px; top: 112px; width: 571px;
  }

  .title {
    text-align: center; font-family: "Cinzel", "Times New Roman", serif; font-weight: 700;
    font-size: 34px; letter-spacing: 14px; color: var(--ink-title);
    margin-bottom: 40px;
  }

  .initial {
    float: left; width: 96px; height: 96px; margin: 4px 12px 4px 0;
    background: linear-gradient(135deg, var(--cap-green), var(--cap-red));
    border: 2px solid var(--frame-gold);
  }

  .body-copy {
    font-size: 15px; line-height: 22px; text-align: justify;
    margin-bottom: 30px;
  }
  .body-copy.lead { margin-bottom: 34px; }

  .ledger-block { position: relative; padding-top: 4px; }
  .house-sketch {
    position: absolute; left: 20px; right: 20px; top: 50px; height: 300px;
    background: linear-gradient(180deg, rgba(226,210,174,0) 0%, var(--house-light) 30%, var(--house-dark) 100%);
    opacity: .55;
  }

  .ledger-heading {
    position: relative;
    font-family: "IM Fell English SC", "Times New Roman", serif; font-weight: 400;
    font-size: 40px; line-height: 48px; color: var(--ink-title);
    margin-bottom: 12px;
  }

  .ledger {
    position: relative; width: 100%;
    border-collapse: collapse; font-size: 14px; line-height: 20px;
  }
  .ledger td { padding: 0; vertical-align: top; }
  .ledger .date { width: 250px; }

  .presenter {
    position: relative; text-align: center; color: var(--ink-title);
    margin-top: 60px;
  }
  .presenter .by { font-style: italic; font-size: 13px; display: block; }
  .presenter .name { font-weight: 700; font-size: 17px; letter-spacing: 1px; }
</style>
</head>
<body>
  <div class="frame" role="img" aria-label="Ornate dark aged-paper border with scrolled corners"></div>
  <div class="parchment"></div>

  <main class="content">
    <h1 class="title">MARROWBROOK</h1>

    <p class="body-copy lead"><span class="initial" role="img" aria-label="Illuminated initial letter M with vine ornament"></span>arrowbrook is a neighborhood in the City of Port Alder. Located east of Briar Heights, Marrowbrook is bordered by 9th Avenue to the west and 12th Avenue and Cooper's Run to the east. Initially developed in 1954, an addition was added in 1956. It is located in a beautiful area of America's 1st Settlement (1559), Port Alder, Florida encompassed with towering pine trees and breathtaking heritage oaks.</p>

    <p class="body-copy">The land comprising Marrowbrook was originally owned by Tomás Varela under a Spanish Land Grant and affirmed by President Andrew Whitcomb on September 7, 1835. Spain relinquished Florida to the United States in 1819 under the Ardent-Osla Treaty and lands previously granted to settlers prior thereto were honored if claims were filed and approved by the United States government.</p>

    <p class="body-copy">Through the years, the land changed hands many times but was eventually developed into the Marrowbrook subdivision in 1954, by Wendell Ashby, President of Marrowbrook, Inc. The subdivision contains 63 lots with a beautiful, oak-filled park located just off of Thimble Street.</p>

    <p class="body-copy">Built in 1957 and containing approximately 2600 square feet of living, garage and patio space, the home located at 418 Larkspur Lane is a trip back in time to when houses were carefully planned catering to modern sensibilities, neither too big nor too small, neither too formal nor too casual.</p>

    <section class="ledger-block">
      <div class="house-sketch" role="img" aria-label="Faded sketch of the mid-century home and its oak trees"></div>

      <h2 class="ledger-heading">Ledger of Hearth</h2>

      <table class="ledger">
        <tr><td class="date">September 7, 1835</td><td>Tomás Varela, Spanish Land Grant</td></tr>
        <tr><td class="date">April 27, 1954</td><td>Marrowbrook Plat approved by Alder County</td></tr>
        <tr><td class="date">April 27, 1957</td><td>Wendell Ashby, III and Marian W. Ashby</td></tr>
        <tr><td class="date">September 20, 1960</td><td>Harriet Lee Dorsey (Pruitt)</td></tr>
        <tr><td class="date">February 13, 1961</td><td>Walter M. Kinsley and Edna E. Kinsley</td></tr>
        <tr><td class="date">January 10, 1989</td><td>Russell A. Garner</td></tr>
        <tr><td class="date">September 8, 2010</td><td>Russell A. Garner and Lorna Jean Whitfield</td></tr>
      </table>

      <p class="presenter"><span class="by">Presented by</span><span class="name">Ledger of Hearth, LLC</span></p>
    </section>
  </main>
</body>
</html>
```